Oversized Post Card for Busines Owners 1st 2nd and 3rd prizes

Create a professional, fresh and polished oversized post card for law firm specializing in Business Law, Succession Planning, and Employment Law

Use any picture(s) of your choice (mine or ones you recommend), logo, headshot and company info

www.morvenashcroftlegal.example

Brookhaven Office - 4800 Tillman Road, Suite 1400, Charlotte, NC 28219
Whitcombe Office - 13540 Quarry Lane, Suite 300, Charlotte, NC 28269

Phone (704) 555-0187

Use this card for a Free Consultation

Target Market(s)

Business Owners (of small businesses)

Industry/Entity Type

Business

Font styles to use
Serif
Sans Serif

Requirements
Must have
• Company name, logo and contact info
• Serving business owners with legal guidance
• Business Law, Succession Planning & Wealth Transfers
• www.morvenashcroftlegal.example
• Brookhaven Office - 4800 Tillman Road, Suite 1400, Charlotte, NC 28219
• Whitcombe Office - 13540 Quarry Lane, Suite 300, Charlotte, NC 28269
• Phone (704) 555-0187
• Use this card for a Free Consultation
Nice to have
• pictures (yours or mine) - you choose; headshot picture

```html
<!DOCTYPE html>
<html lang="en">
<head>
<meta charset="utf-8">
<title>Morven Ashcroft Law PLLC – Postcard</title>
<link href="https://fonts.googleapis.com/css2?family=PT+Sans+Narrow:wght@400;700&family=Cormorant+Garamond:wght@500&display=swap" rel="stylesheet">
<style>
  :root{
    --blue:#0b7cab;
    --blue-deep:#0c4466;
    --navy:#0a3350;
    --silver-dark:#7d8185;
    --white:#ffffff;
    --ink:#333333;
    --stage:#c4c4c4;
  }
  *{margin:0;padding:0;box-sizing:border-box}
  html,body{width:1003px;height:1200px;overflow:hidden;background:var(--stage)}
  .canvas{position:relative;width:1003px;height:1200px}
  .card{position:absolute;left:90px;width:822px;height:530px;background:var(--white);overflow:hidden}
  .card--front{top:32px}
  .card--back{top:610px}
  .card svg.shapes{position:absolute;left:0;top:0;width:822px;height:530px}
  .abs{position:absolute}

  .brand{position:absolute;text-align:center}
  .brand__rule{height:1px;background:var(--ink)}
  .brand__name{font-family:"PT Sans Narrow",sans-serif;font-weight:700;color:var(--blue);white-space:nowrap}
  .brand__suffix{display:flex;align-items:center;gap:8px;font-family:"Cormorant Garamond",serif;font-weight:500;color:var(--ink);letter-spacing:1px}
  .brand__suffix::before,.brand__suffix::after{content:"";flex:1;height:1px;background:var(--ink)}
  .brand__dot{position:absolute;border-radius:50%;background:var(--blue-deep)}

  .front__brand{left:51px;top:130px;width:298px}
  .front__brand .brand__name{font-size:38px;line-height:60px}
  .front__brand .brand__suffix{font-size:17px;line-height:20px}
  .front__brand .brand__dot{left:109px;top:-110px;width:82px;height:82px}

  .headline{left:0;width:822px;text-align:center;color:var(--white);font-family:"PT Sans Narrow",sans-serif;font-weight:700;white-space:nowrap}
  .headline--main{top:318px;font-size:72px;line-height:76px;letter-spacing:-0.5px}
  .headline--sub{top:386px;font-size:27px;line-height:32px}

  .contact-row{left:0;top:480px;width:822px;display:flex;justify-content:center;align-items:center;gap:18px;color:var(--blue);font-family:"PT Sans Narrow",sans-serif;font-weight:700}
  .contact-row__phone{display:flex;align-items:center;gap:6px;font-size:30px}
  .contact-row__sep{width:1px;height:24px;background:var(--silver-dark)}
  .contact-row__web{font-size:21px}

  .back__brand{left:42px;top:22px;width:171px}
  .back__brand .brand__name{font-size:20px;line-height:32px}
  .back__brand .brand__suffix{font-size:10px;line-height:14px;gap:5px}

  .office{text-align:right;font-family:"PT Sans Narrow",sans-serif}
  .office__title{font-weight:700;font-size:13px;color:var(--blue);line-height:16px;text-transform:uppercase}
  .office__line{font-size:11px;line-height:14px;color:var(--blue)}
  .office--one{right:calc(822px - 305px);top:113px}
  .office--two{right:calc(822px - 329px);top:187px}

  .services{left:12px;width:350px;top:268px;text-align:center;color:var(--white);font-family:"PT Sans Narrow",sans-serif;font-size:14px;line-height:18px}
  .cta{left:23px;width:280px;top:346px;text-align:center;color:var(--white);font-family:"PT Sans Narrow",sans-serif;font-weight:700}
  .cta__label{font-size:22px;line-height:22px;letter-spacing:0.3px}
  .cta__phone{font-size:30px;line-height:34px;margin-top:4px}
  .cta__web{font-size:15px;line-height:18px}

  .stamp-box{left:682px;top:25px;width:121px;height:91px;border:1px solid #bdbdbd}
  .address-line{left:430px;width:364px;height:1px;background:#8a8a8a}
</style>
</head>
<body>
<main class="canvas">

  <section class="card card--front">
    <svg class="shapes" viewBox="0 0 822 530">
      <defs>
        <linearGradient id="photoTone" x1="0" y1="0" x2="1" y2="0">
          <stop offset="0" stop-color="#ffffff"/>
          <stop offset="0.12" stop-color="#f1e6cf"/>
          <stop offset="0.35" stop-color="#c9a25a"/>
          <stop offset="0.6" stop-color="#d48a3a"/>
          <stop offset="1" stop-color="#b9622e"/>
        </linearGradient>
        <linearGradient id="bandFront" x1="0" y1="0" x2="1" y2="0">
          <stop offset="0" stop-color="#0a3a5a"/>
          <stop offset="0.45" stop-color="#0b6a96"/>
          <stop offset="1" stop-color="#0b80b0"/>
        </linearGradient>
        <linearGradient id="silverFront" x1="0" y1="0" x2="1" y2="0">
          <stop offset="0" stop-color="#6e7276"/>
          <stop offset="0.5" stop-color="#e4e6e8"/>
          <stop offset="1" stop-color="#8c9094"/>
        </linearGradient>
      </defs>
      <rect x="150" y="0" width="672" height="300" fill="url(#photoTone)" role="img" aria-label="Photo of confident small business owners standing together outdoors in warm autumn light"/>
      <path d="M430,300 C600,290 720,260 822,212 L822,190 C720,240 600,270 430,300 Z" fill="url(#silverFront)"/>
      <path d="M0,244 C250,300 520,310 822,206 L822,484 C650,430 350,410 0,505 Z" fill="url(#bandFront)"/>
      <path d="M0,505 C350,410 650,430 822,484 L822,490 C640,440 360,425 0,528 Z" fill="url(#silverFront)"/>
    </svg>

    <div class="brand front__brand">
      <span class="brand__dot" aria-hidden="true"></span>
      <div class="brand__rule"></div>
      <div class="brand__name">Morven Ashcroft</div>
      <div class="brand__suffix">LAW PLLC</div>
    </div>

    <h1 class="abs headline headline--main">FREE CONSULTATION</h1>
    <p class="abs headline headline--sub">Business Law, Succession Planning &amp; Employment Law</p>

    <div class="abs contact-row">
      <span class="contact-row__phone">
        <svg width="24" height="24" viewBox="0 0 24 24" aria-hidden="true"><circle cx="12" cy="12" r="10.5" fill="none" stroke="currentColor" stroke-width="2"/><path d="M8.4 6.8c.4-.3.9-.2 1.1.2l1 1.8c.2.4.1.8-.2 1.1l-.7.6c.5 1.2 1.4 2.2 2.6 2.8l.6-.7c.3-.3.8-.4 1.1-.2l1.8 1c.4.2.5.8.2 1.1l-.9 1c-.5.5-1.300.7-2 .4-2.6-1-4.6-3-5.6-5.6-.2-.7 0-1.5.5-2z" fill="currentColor"/></svg>
        (704) 555-0187
      </span>
      <span class="contact-row__sep"></span>
      <span class="contact-row__web">www.morvenashcroftlegal.example</span>
    </div>
  </section>

  <section class="card card--back">
    <svg class="shapes" viewBox="0 0 822 530">
      <defs>
        <linearGradient id="bandBack" x1="0" y1="0" x2="1" y2="0">
          <stop offset="0" stop-color="#0a3350"/>
          <stop offset="0.5" stop-color="#0b6690"/>
          <stop offset="1" stop-color="#0b80b0"/>
        </linearGradient>
        <linearGradient id="silverBack" x1="0" y1="0" x2="1" y2="1">
          <stop offset="0" stop-color="#e6e8ea"/>
          <stop offset="1" stop-color="#8d9195"/>
        </linearGradient>
      </defs>
      <path d="M0,0 L222,0 C420,70 470,440 220,530 L0,530 Z" fill="url(#bandBack)"/>
      <path d="M200,0 L222,0 C420,70 470,440 220,530 L200,530 C440,430 390,70 200,0 Z" fill="url(#silverBack)"/>
      <path d="M0,0 L178,0 C360,60 410,420 180,530 L0,530 Z" fill="url(#bandBack)"/>
      <path d="M0,0 L178,0 C290,40 345,140 354,254 L0,254 Z" fill="#ffffff"/>
      <rect x="0" y="74" width="162" height="180" fill="#d9c9a6" role="img" aria-label="Headshot of the firm's attorney in a dark blazer"/>
      <circle cx="163" cy="330" r="12" fill="none" stroke="#ffffff" stroke-width="2"/>
      <path d="M159 323.5c.4-.3.8-.2 1 .2l.9 1.6c.2.3.1.7-.2 1l-.6.5c.5 1.1 1.3 2 2.4 2.5l.5-.6c.3-.3.7-.4 1-.2l1.6.9c.3.2.4.7.2 1l-.8.9c-.5.5-1.2.6-1.8.4-2.4-.9-4.2-2.7-5.1-5.1-.2-.6 0-1.300.5-1.8z" fill="#ffffff"/>
    </svg>

    <div class="brand back__brand">
      <div class="brand__rule"></div>
      <div class="brand__name">Morven Ashcroft</div>
      <div class="brand__suffix">LAW PLLC</div>
    </div>

    <div class="abs office office--one">
      <div class="office__title">Brookhaven Office</div>
      <div class="office__line">4800 Tillman Road,</div>
      <div class="office__line">Suite 1400, Charlotte,</div>
      <div class="office__line">NC 28219</div>
    </div>
    <div class="abs office office--two">
      <div class="office__title">Whitcombe Office</div>
      <div class="office__line">13540 Quarry Lane,</div>
      <div class="office__line">Suite 300, Charlotte,</div>
      <div class="office__line">NC 28269</div>
    </div>

    <p class="abs services">Business Law, Succession Planning, Wealth Transfers,<br>Employment Law, Guidance for Business Owners</p>

    <div class="abs cta">
      <div class="cta__label">CALL NOW</div>
      <div class="cta__label">FREE CONSULTATION</div>
      <div class="cta__phone">(704) 555-0187</div>
      <div class="cta__web">www.morvenashcroftlegal.example</div>
    </div>

    <div class="abs stamp-box"></div>
    <div class="abs address-line" style="top:229px"></div>
    <div class="abs address-line" style="top:267px"></div>
    <div class="abs address-line" style="top:306px"></div>
    <div class="abs address-line" style="top:344px"></div>
  </section>

</main>
</body>
</html>
```